Chiropractic Business Card

I need a business card designed to help me stand apart from my competition. I really like simple, clean designs that appear open and inviting. I would like the designs to incorporate the color blue, green, or both. I really like the attached picture because it highlights that I just don't treat "back pain" and it being a nice computer graphic helps show that I have a modern practice. "Modern practice" meaning merging technology and most current research in my patient care.

My information is:

Wesley Harmon, DC
Phone- (707) 555-0182
Email- drwesleyharmon@mailbox-example.com
Website- www.fernleachiropractic-example.com
Address- 248 Pellham Street, Sonoma, CA 95400

Jpeg and pdf attached of Fernlea Chiropractic logo.
Updates

Atmosphere to be clean lines and solid colors to be have gradient fading, but don't want too much going on with the fading. Simple.

Target Market(s)

Active adults who are health conscious between the ages of 20-70

Industry/Entity Type

Computer

Colors
0455a3
85cae6

Requirements
Must have
• Change color of Fernlea chiropractic logo (maroon) to fit the rest of the design.
Nice to have
• Can separate the running image from the black background to have it work with the design.

```html
<!DOCTYPE html>
<html lang="en">
<head>
<meta charset="UTF-8">
<title>Fernlea Chiropractic – Business Card</title>
<link href="https://fonts.googleapis.com/css2?family=Exo+2:wght@500;600&family=Open+Sans:wght@400;600;700&display=swap" rel="stylesheet">
<style>
  :root {
    --backdrop: #2f2f31;
    --card: #ffffff;
    --card-shade: #f1f2f4;
    --indigo: #3c3ca0;
    --sky: #1ba6df;
    --ink: #2c2c2c;
    --white: #ffffff;
  }
  * { margin: 0; padding: 0; box-sizing: border-box; }
  html, body {
    width: 1200px;
    height: 816px;
    overflow: hidden;
    background: var(--backdrop);
  }
  .card {
    position: absolute;
    left: 80px;
    top: 111px;
    width: 1040px;
    height: 594px;
    border-radius: 44px;
    background: radial-gradient(ellipse at 45% 40%, var(--card) 55%, var(--card-shade) 100%);
    overflow: hidden;
    font-family: "Open Sans", Arial, sans-serif;
    color: var(--ink);
  }
  .brand {
    position: absolute;
    top: 70px;
    right: 70px;
    display: flex;
    align-items: center;
    gap: 14px;
  }
  .brand-mark {
    width: 30px;
    height: 30px;
    background: var(--indigo);
  }
  .brand-name {
    font-family: "Open Sans", Arial, sans-serif;
    font-weight: 700;
    font-size: 34px;
    letter-spacing: 0.5px;
    color: var(--indigo);
  }
  .divider {
    position: absolute;
    left: 380px;
    right: 0;
    top: 272px;
    height: 3px;
    background: var(--sky);
  }
  .name-band {
    position: absolute;
    left: 0;
    top: 262px;
    width: 390px;
    height: 92px;
    border-radius: 0 46px 46px 0;
    background: var(--indigo);
    color: var(--white);
    font-family: "Exo 2", Arial, sans-serif;
    text-align: right;
    padding: 14px 42px 0 0;
  }
  .person-name {
    font-size: 29px;
    font-weight: 600;
    line-height: 1.15;
  }
  .person-title {
    font-size: 20px;
    font-weight: 500;
    letter-spacing: 1.5px;
    line-height: 1.5;
  }
  .contact-list {
    position: absolute;
    left: 62px;
    top: 410px;
    list-style: none;
  }
  .contact-list li {
    display: flex;
    align-items: center;
    gap: 16px;
    height: 40px;
    font-size: 20px;
  }
  .icon {
    width: 22px;
    height: 22px;
    fill: var(--indigo);
    flex: none;
  }
  .address {
    position: absolute;
    left: 640px;
    top: 308px;
    display: flex;
    align-items: flex-start;
    gap: 14px;
    font-size: 21px;
    line-height: 1.45;
  }
  .address .icon { margin-top: 22px; }
</style>
</head>
<body>
  <div class="card">
    <div class="brand">
      <span class="brand-mark"></span>
      <span class="brand-name">Fernlea Chiropractic</span>
    </div>

    <div class="divider"></div>

    <div class="name-band">
      <div class="person-name">Wesley Harmon, DC</div>
      <div class="person-title">GENERAL MANAGER</div>
    </div>

    <div class="address">
      <svg class="icon" viewBox="0 0 24 24" aria-hidden="true"><path d="M12 3 2 12h3v9h5v-6h4v6h5v-9h3z"/></svg>
      <div>248 Pellham Street,<br>Sonoma, CA 95400</div>
    </div>

    <ul class="contact-list">
      <li>
        <svg class="icon" viewBox="0 0 24 24" aria-hidden="true"><path d="M6.6 10.8a15.1 15.1 0 0 0 6.6 6.6l2.2-2.2c.3-.3.7-.4 1-.2 1.1.4 2.3.6 3.6.6.6 0 1 .4 1 1V20c0 .6-.4 1-1 1A17 17 0 0 1 3 4c0-.6.4-1 1-1h3.5c.6 0 1 .4 1 1 0 1.3.2 2.5.6 3.6.1.3 0 .7-.2 1z"/></svg>
        <span>(707) 555-0182</span>
      </li>
      <li>
        <svg class="icon" viewBox="0 0 24 24" aria-hidden="true"><path d="M2 5h20v14H2z" fill="none"/><path d="M3 5h18a1 1 0 0 1 1 1v.4l-10 6.3L2 6.4V6a1 1 0 0 1 1-1zm-1 3.7 10 6.3 10-6.3V18a1 1 0 0 1-1 1H3a1 1 0 0 1-1-1z"/></svg>
        <span>drwesleyharmon@mailbox-example.com</span>
      </li>
      <li>
        <svg class="icon" viewBox="0 0 24 24" aria-hidden="true"><path d="M12 2a10 10 0 1 0 0 20 10 10 0 0 0 0-20zm6.9 6h-3a15 15 0 0 0-1.3-3.9A8 8 0 0 1 18.9 8zM12 4c.8 1.2 1.5 2.5 1.9 4h-3.8c.4-1.5 1.1-2.8 1.9-4zM4.3 14a8 8 0 0 1 0-4h3.4a16 16 0 0 0 0 4zm.8 2h3a15 15 0 0 0 1.3 3.9A8 8 0 0 1 5.1 16zm3-8h-3a8 8 0 0 1 4.3-3.9A15 15 0 0 0 8.1 8zM12 20c-.8-1.2-1.5-2.5-1.9-4h3.8c-.4 1.5-1.1 2.8-1.9 4zm2.3-6H9.7a14 14 0 0 1 0-4h4.6a14 14 0 0 1 0 4zm.3 5.9a15 15 0 0 0 1.3-3.9h3a8 8 0 0 1-4.3 3.9zm1.7-5.9a16 16 0 0 0 0-4h3.4a8 8 0 0 1 0 4z"/></svg>
        <span>www.fernleachiropractic-example.com</span>
      </li>
    </ul>
  </div>
</body>
</html>
```